Recruitment Web Site Design

I need a Recruitment website explaining who we are and what services we deliver.
This is a new company and the image we portray is extremely important. Must be very professional.
Our target marget are bluechip companies and professionals including executives.

The final design should communicate connecting professionals matching company and individual needs.

Target Market(s)

Corporate, Blue Chip Companies, Professionals/Executives

Industry/Entity Type

It Company

Requirements
Must have
• Must be professional and Sophisticated.
Must have a few tabs.

Must be unique to the norm of websites as I am looking for something different.
Nice to have
• Good graphics with people connecting. Multi - racial pics will be good as we are in South Africa and diversity is a must.
Also a front page (be unique).

I am putting this out there for you to use your imagination and come up with something brilliant.

A few websites you can base ideas from

www.copperlantern.com
www.ovalquay.co.za
www.kel.co.za
www.rux.co.za

```html
<!DOCTYPE html>
<html lang="en">
<head>
<meta charset="utf-8">
<title>Corvane Recruitment</title>
<link rel="stylesheet" href="https://fonts.googleapis.com/css2?family=Kalam:wght@400&family=PT+Sans:wght@400;700&family=Oswald:wght@300&display=swap">
<style>
:root{
  --bg-top:#d2d2d2;
  --bg-bottom:#a5a5a5;
  --ink:#222;
  --black:#111;
  --red:#d40b0b;
  --white:#fff;
  --line:#8d8d8d;
}
*{margin:0;padding:0;box-sizing:border-box}
html,body{width:1200px;height:1099px;overflow:hidden}
body{
  background:linear-gradient(180deg,var(--bg-top) 0%,#bdbdbd 45%,var(--bg-bottom) 100%);
  font-family:"PT Sans",Arial,sans-serif;color:var(--ink);position:relative;
}
a{color:inherit;text-decoration:none}
.header{
  position:absolute;left:153px;top:0;width:894px;height:104px;
  background:linear-gradient(180deg,#fff 0%,#e6e6e6 60%,#d4d4d4 100%);
}
.brand{position:absolute;left:12px;top:24px;display:flex;align-items:center;gap:18px}
.brand-mark{width:56px;height:56px;background:var(--red)}
.brand-name{font-family:"PT Sans",sans-serif;color:#3b3b3b;font-weight:400;line-height:1}
.brand-name .main{display:block;font-size:31px;letter-spacing:5px}
.brand-name .sub{display:block;font-size:10px;letter-spacing:6px;margin-top:6px;padding-left:18px}
.account{position:absolute;right:14px;top:0;height:26px;background:var(--black);display:flex;align-items:center;padding:0 12px;font-size:12px;color:#fff}
.account a{padding:0 8px}
.account a+a{border-left:1px solid #555}
.search{position:absolute;right:16px;top:54px;display:flex;height:25px}
.search input{width:126px;border:0;background:#fff}
.search button{border:0;background:var(--red);color:#fff;font:11px "PT Sans",sans-serif;padding:0 5px}
.nav{position:absolute;left:161px;top:106px;display:flex;gap:7.5px}
.nav a{width:141px;height:29px;background:var(--black);color:#fff;font-size:12px;display:flex;align-items:center;justify-content:center}
.hero{
  position:absolute;left:160px;top:140px;width:881px;height:330px;
  background:linear-gradient(180deg,#fff 0%,#ececec 100%);
  box-shadow:0 2px 4px rgba(0,0,0,.35);
}
.hero-text{position:absolute;left:29px;top:62px;width:230px}
.script{font-family:"Kalam",cursive;font-weight:400;color:#333}
.hero-text h1{font-size:31px;margin-bottom:10px}
.hero-text p{font-size:12px;line-height:18.5px;color:#444}
.hero-photo{position:absolute;left:271px;top:0;width:610px;height:330px;
  background:linear-gradient(90deg,#f2f2f2 0%,#c9b8a8 20%,#3a3a3a 40%,#9aa8c8 70%,#1d1d1d 100%)}
.dots{position:absolute;left:28px;top:315px;display:flex;gap:2px}
.dots span{width:9px;height:9px;border-radius:50%;background:var(--black)}
.dots span.active{background:var(--red)}
.candidates{position:absolute;left:159px;top:486px;width:259px}
.candidates h2{font-size:26px;line-height:36px;margin-bottom:8px}
.candidates .lead a{display:block;font-size:13px;font-weight:700;line-height:20.5px;color:#111}
.candidates ul{list-style:none;margin-top:5px}
.candidates li{font-size:12px;line-height:20.3px;color:#222}
.more{display:block;font-size:12.5px;font-weight:700;color:#111}
.candidates .more{margin-top:6px}
.divider{position:absolute;left:418px;top:497px;width:1px;height:232px;background:var(--line)}
.panel{
  position:absolute;left:441px;width:285px;height:106px;
  background:linear-gradient(110deg,#d8d8d8 0%,#f7f7f7 45%,#c9c9c9 100%);
  border:1px solid #999;
}
.panel h2{position:absolute;left:19px;top:11px;font-size:25px}
.panel .links{position:absolute;left:0;right:0;top:57px;display:flex;justify-content:center;
  font-family:"Oswald",sans-serif;font-weight:300;font-size:18.5px;color:#111}
.panel .links span{padding:0 6px}
.panel .links span+span{border-left:1px solid #888}
.howwork{position:absolute;left:746px;top:484px}
.howwork h2{font-size:26px;line-height:36px}
.video{position:absolute;left:747px;top:526px;width:293px;height:188px;
  background:linear-gradient(135deg,#c7a46a 0%,#e8dcc4 40%,#8c4b4b 60%,#ede6da 100%);
  box-shadow:0 2px 4px rgba(0,0,0,.45)}
.video svg{position:absolute;left:126px;top:72px}
.features{position:absolute;left:158px;top:747px;width:883px;height:196px;background:var(--white);display:flex}
.feature{width:213px;border-right:1px solid #ccc;padding:19px 0 0 29px}
.feature h2{font-size:25px;line-height:34px;margin-bottom:7px}
.feature ul{list-style:none}
.feature li{font-size:12px;line-height:20.3px;color:#222}
.feature .more{margin-top:8px}
.newsletter{flex:1;padding:19px 15px 0 31px;border-right:0}
.newsletter h2{margin-bottom:8px}
.newsletter input{display:block;width:100%;height:25px;border:1px solid #aaa;margin-bottom:8px;
  padding-left:7px;font:12px "PT Sans",sans-serif;color:#222}
.newsletter input::placeholder{color:#222}
.newsletter button{float:right;background:var(--red);color:#fff;border:0;height:24px;padding:0 8px;font:12.5px "PT Sans",sans-serif}
.rule{position:absolute;left:158px;top:948px;width:885px;height:6px;background:var(--black)}
.footer{position:absolute;left:158px;top:954px;width:885px;height:145px;
  background:linear-gradient(180deg,#fff 0%,#f1f1f1 40%,#c9c9c9 100%);text-align:center;font-size:11px}
.footer nav{margin-top:52px}
.footer nav a{padding:0 5px}
.footer nav a+a{border-left:1px solid #333}
.footer p{margin-top:10px}
</style>
</head>
<body>
<header class="header">
  <div class="brand">
    <div class="brand-mark"></div>
    <div class="brand-name"><span class="main">CORVANE</span><span class="sub">RECRUITMENT</span></div>
  </div>
  <div class="account"><a href="#">Login</a><a href="#">Register</a></div>
  <form class="search"><input type="text" aria-label="Search"><button type="button">SEARCH</button></form>
</header>

<nav class="nav">
  <a href="#">Home</a><a href="#">Candidates</a><a href="#">Clients</a><a href="#">Who we are</a><a href="#">Blog</a><a href="#">Contact Us</a>
</nav>

<section class="hero">
  <div class="hero-photo" role="img" aria-label="Group of five diverse smiling professionals in business attire"></div>
  <div class="hero-text">
    <h1 class="script">Heading</h1>
    <p>Lorem Ipsum is simply dummy text of the printing and typesetting industry. Lorem Ipsum has been the industry's standard dummy text ever since the 1500s, when an unknown printer took..</p>
  </div>
  <div class="dots"><span></span><span></span><span class="active"></span><span></span><span></span><span></span></div>
</section>

<section class="candidates">
  <h2 class="script">Candidates</h2>
  <div class="lead"><a href="#">Send us your CV»</a><a href="#">Search jobs»</a><a href="#">Why use CORVANE?»</a></div>
  <ul>
    <li>What our candidates say about us»</li>
    <li>Sources for continuing professional education»</li>
    <li>How to write a great CV»</li>
    <li>How to write a great cover letter»</li>
    <li>Tips &amp; tricks for a successful interview»</li>
  </ul>
  <a class="more" href="#">more &gt;&gt;</a>
</section>
<div class="divider"></div>

<div class="panel" style="top:501px">
  <h2 class="script">Job Seekers</h2>
  <div class="links"><span>JOB SEARCH</span><span>SUBMIT RESUME</span></div>
</div>
<div class="panel" style="top:620px">
  <h2 class="script">Employers</h2>
  <div class="links"><span>PROPOSAL</span><span>PROCESS</span><span>TESTIMONIALS</span></div>
</div>

<section class="howwork"><h2 class="script">How we work</h2></section>
<div class="video" role="img" aria-label="Video still of an office interview with a document being handed over">
  <svg width="40" height="40" viewBox="0 0 40 40" aria-hidden="true">
    <circle cx="20" cy="20" r="19" fill="#d40b0b" stroke="#8a0000"/>
    <path d="M15 11 L29 20 L15 29 Z" fill="#2a2a2a"/>
  </svg>
</div>

<section class="features">
  <div class="feature">
    <h2 class="script">Clients</h2>
    <ul><li>Case studies &amp; success stories»</li><li>What our clients say about us»</li><li>Executive search / headhunting»</li><li>Outplacement services»</li></ul>
    <a class="more" href="#">more &gt;&gt;</a>
  </div>
  <div class="feature" style="width:232px">
    <h2 class="script">Testimonials</h2>
    <ul><li>Case studies &amp; success stories»</li><li>What our clients say about us»</li><li>Executive search / headhunting»</li><li>Outplacement services»</li></ul>
    <a class="more" href="#">more &gt;&gt;</a>
  </div>
  <div class="feature" style="width:212px">
    <h2 class="script">News</h2>
    <ul><li>Case studies &amp; success stories»</li><li>What our clients say about us»</li><li>Executive search / headhunting»</li><li>Outplacement services»</li></ul>
    <a class="more" href="#">more &gt;&gt;</a>
  </div>
  <form class="feature newsletter">
    <h2 class="script">Newsletter</h2>
    <input type="text" placeholder="Enter the Name">
    <input type="email" placeholder="Enter the E mail id">
    <button type="button">Sign Up</button>
  </form>
</section>

<div class="rule"></div>
<footer class="footer">
  <nav><a href="#">Home</a><a href="#">Candidates</a><a href="#">Clients</a><a href="#">Who we are</a><a href="#">Blog</a><a href="#">Contact Us</a></nav>
  <p>Copyrights @ 2012 All Rights Reserved</p>
</footer>
</body>
</html>
```